Poster for a 100 y.o. Tennis Tournament

I would like a poster designed to promote our tennis tournament but I'd like to avoid some of the clichés like the shadow of a player serving. Just well styled text would be fine but some clever imagery would be a bonus.
Highlighting the fact our tournament has been running for over 100 years would be nice so a retro design would work. But that doesn't mean a modern design, for example a minimalist approach utilising the lines of a tennis court, wouldn't work.
Updates

Our tennis committee is now in the process of short listing and will provide an update within 48 hours.

Industry/Entity Type

Court

Requirements
Must have
• The poster must contain the following text at a minimum:
"Marbury Tennis Tournament"/"Since 1908"
"9 March - 11 March, 2013" or "9-11 March, 2013", etc
"www.marburytennis.com.au"

The poster must be reproducible in colour and black & white, or at least have an alternate for black & white.

The poster must be usable in both A3 and A4 sizes.
Nice to have
• The poster should contain the following text:
"Championship"
"Handicap"
"Seniors"
"Juniors"
Each above may be optionally succeeded by "Singles & Doubles", e.g. "Championship Singles & Doubles". It would actually be clearer if this additional text was used but would be repetitive, so alternate text "Singles & Doubles in all categories" might also be used. Alternatives for variety (with the first word the focus): "Championship Singles & Doubles", "Handicap Singles & Doubles", "Seniors 35+ & 50+", "Juniors 18&U, 14&U"

Ideally the poster will provision room for four to eight sponsors logos, preferably at the bottom, but failure to do this is not a show stopper.

The following text may also be used:
"Entries close February 24"
"Tollard Plate Weekend"

Attached is a photo of one of the old trophies. Utilisation of the curved style of the "Marbury Tennis Tournament" text would fit in with the history if the tournament.

The ability to reuse elements of the poster in a single page website used to promote the tournament would be an advantage (as it will provide consistency).

If you could have an image of a tennis ball that conveys the same energy as the clock/tyre image in the attached "Under the Glass Moon" poster, that would be cool. Or using split imagery of a wooden racquet and a modern racquet, but with some energy, would also be good. These are just ideas though and by no means essential.

I've also attached a photo of a t-shirt with a poster layout I thought looked good.

Some additional text that can be used:
"Brand new courts"
"Brindle Park, Oakhurst Tce, Marbury"
"Phone 0427 318 642"
"Prizes and Trophies"

```html
<!DOCTYPE html>
<html lang="en">
<head>
<meta charset="utf-8">
<title>Marbury Tennis Tournament 2013</title>
<link rel="stylesheet" href="https://fonts.googleapis.com/css2?family=Anton&family=Yanone+Kaffeesatz:wght@300;400&display=swap">
<style>
  :root {
    --sage: #b4c598;
    --sage-pale: #cfd6b4;
    --cream: #e6e5cc;
    --crimson: #8a1717;
    --crimson-dark: #2b0707;
    --ink: #111111;
    --white: #ffffff;
  }
  html, body {
    margin: 0;
    padding: 0;
    overflow: hidden;
    background: var(--sage);
  }
  .poster {
    position: relative;
    width: 856px;
    height: 1200px;
    overflow: hidden;
    background: var(--sage);
    font-family: "Yanone Kaffeesatz", "Arial Narrow", sans-serif;
  }
  .edge-bar {
    position: absolute;
    left: 20px;
    top: 22px;
    width: 76px;
    height: 460px;
    background: var(--ink);
  }
  .pale-field {
    position: absolute;
    left: 26px;
    top: 640px;
    width: 820px;
    height: 440px;
    background: linear-gradient(160deg, var(--cream), var(--sage-pale) 55%, var(--sage));
    opacity: 0.85;
  }
  .masthead {
    position: absolute;
    left: 0;
    top: 0;
    width: 856px;
    height: 520px;
  }
  .masthead text {
    font-family: "Anton", "Impact", sans-serif;
    fill: var(--crimson);
    stroke: var(--crimson-dark);
    stroke-width: 4px;
    paint-order: stroke;
  }
  .since {
    position: absolute;
    right: 32px;
    top: 462px;
    margin: 0;
    font-size: 44px;
    font-weight: 300;
    color: var(--ink);
  }
  .dates {
    position: absolute;
    left: 66px;
    top: 540px;
    margin: 0;
    font-family: "Anton", "Impact", sans-serif;
    font-style: italic;
    font-size: 56px;
    letter-spacing: 0.5px;
    color: var(--ink);
    transform: skewX(-6deg);
    white-space: nowrap;
  }
  .categories {
    position: absolute;
    left: 48px;
    top: 626px;
    margin: 0;
    padding: 0;
    list-style: none;
  }
  .categories li {
    font-size: 74px;
    font-weight: 300;
    line-height: 74px;
    color: var(--crimson);
  }
  .formats {
    position: absolute;
    left: 458px;
    top: 668px;
    margin: 0;
    width: 360px;
    font-size: 56px;
    font-weight: 300;
    line-height: 56px;
    text-align: center;
    color: var(--ink);
    transform: rotate(-15deg);
    transform-origin: center;
  }
  .entries {
    position: absolute;
    left: 0;
    width: 856px;
    top: 970px;
    margin: 0;
    text-align: center;
    font-size: 40px;
    font-weight: 400;
    line-height: 46px;
    color: var(--ink);
  }
  .entries span { display: block; }
  .entries .close { padding-left: 60px; }
  .footer-band {
    position: absolute;
    left: 0;
    bottom: 0;
    width: 856px;
    height: 110px;
    background: var(--ink);
    display: flex;
    align-items: center;
    justify-content: center;
  }
  .website {
    margin: 0;
    font-size: 60px;
    font-weight: 300;
    letter-spacing: 1.5px;
    color: var(--white);
  }
</style>
</head>
<body>
<main class="poster">
  <div class="edge-bar"></div>
  <div class="pale-field" role="img" aria-label="Faint embossed tennis player outline on a pale distressed panel"></div>

  <svg class="masthead" viewBox="0 0 856 520" aria-label="Marbury Tennis Tournament">
    <g transform="rotate(5 430 260)">
      <text x="130" y="205" textLength="650" lengthAdjust="spacingAndGlyphs"><tspan font-size="170">M</tspan><tspan font-size="118">ARBURY </tspan><tspan font-size="200">T</tspan><tspan font-size="138">ENNIS</tspan></text>
      <text x="150" y="470" textLength="570" lengthAdjust="spacingAndGlyphs"><tspan font-size="290">T</tspan><tspan font-size="168">OURNAMENT</tspan></text>
    </g>
  </svg>

  <p class="since">*Since 1908</p>
  <p class="dates">9 March – 11 March&nbsp; 2013</p>

  <ul class="categories">
    <li>Championship</li>
    <li>Handicap</li>
    <li>Seniors</li>
    <li>Juniors</li>
  </ul>

  <p class="formats">Singles &amp;<br>Doubles<br>in all categories</p>

  <p class="entries">
    <span class="close">Entries close February 24</span>
    <span>Tollard Plate Weekend</span>
  </p>

  <footer class="footer-band">
    <p class="website">www.marburytennis.com.au</p>
  </footer>
</main>
</body>
</html>
```